Business cards for Harbourline Supply Pty Ltd that import building products into Australia from China
Target Market(s)
Business to Business
Industry/Entity Type
Business
Contact Information for Business Card
Front: Logo and Business Name
Rear:
Vernon Ashcombe
General Manager
Mobile: 0427 619 354
email: vern@harbourlinesupply.com.au
alternative email: vern@coastwardgoods.com.au
web: www.harbourlinesupply.com.au
Adelaide, Brisbane and Darwin
Colors
ec1f27
fbee3d

```html
<!DOCTYPE html>
<html lang="en">
<head>
<meta charset="utf-8">
<title>Harbourline Supply – Business Cards</title>
<link rel="stylesheet" href="https://fonts.googleapis.com/css2?family=Cinzel:wght@500&family=Lato:wght@400;700&family=Open+Sans:wght@800&display=swap">
<style>
  :root {
    --brand-red: #ec1f27;
    --brand-yellow: #fbee3d;
    --front-orange: #f0521f;
    --front-deep: #e63d1c;
    --paper: #ffffff;
    --ink: #3a3a3a;
    --ink-soft: #555555;
    --backdrop: #e4e5e7;
  }
  * { box-sizing: border-box; margin: 0; padding: 0; }
  html, body {
    width: 1200px; height: 1200px; overflow: hidden;
    background: var(--backdrop);
  }
  .sheet {
    width: 1200px; height: 1200px;
    display: flex; flex-direction: column; align-items: center; justify-content: center;
    gap: 60px;
  }
  .card {
    width: 840px; height: 510px; position: relative; overflow: hidden;
    box-shadow: 0 10px 30px rgba(0,0,0,0.12);
  }

  /* Front */
  .card--front {
    background: radial-gradient(ellipse at 50% 58%, var(--brand-yellow) 0%, #fdb52a 25%, #f7852a 50%, var(--front-orange) 75%, var(--front-deep) 100%);
    display: flex; align-items: center; justify-content: center;
  }
  .front-name {
    font-family: "Open Sans", Arial, sans-serif;
    font-weight: 800; font-size: 60px; letter-spacing: 1px;
    color: var(--paper); text-transform: uppercase;
  }

  /* Rear */
  .card--rear { background: var(--paper); }
  .rear-name {
    position: absolute; top: 62px; left: 0; right: 0; text-align: center;
    font-family: "Cinzel", Georgia, serif; font-weight: 500;
    font-size: 50px; color: var(--brand-red); letter-spacing: 1px;
  }
  .person { position: absolute; top: 142px; left: 0; right: 0; text-align: center; }
  .person-name {
    font-family: "Lato", Arial, sans-serif; font-size: 32px;
    color: var(--brand-red); text-transform: uppercase; letter-spacing: 1px;
  }
  .person-role {
    font-family: "Lato", Arial, sans-serif; font-size: 18px; color: var(--ink-soft);
    margin-top: 2px;
  }
  .band-rule {
    position: absolute; left: 0; right: 0; height: 2px; background: var(--brand-yellow);
  }
  .band-rule--top { top: 238px; }
  .band-rule--bottom { top: 366px; }
  .contact-band {
    position: absolute; top: 248px; left: 0; right: 0; height: 110px;
    background: var(--brand-red);
    display: flex; align-items: center; justify-content: center;
    font-family: "Lato", Arial, sans-serif; font-size: 20px; color: var(--paper);
  }
  .contact-col { display: flex; flex-direction: column; gap: 10px; }
  .contact-col--left { align-items: flex-end; padding-right: 18px; }
  .contact-col--right { align-items: flex-start; padding-left: 18px; }
  .contact-divider { width: 1px; height: 66px; background: rgba(255,255,255,0.8); }
  .contact-item { display: flex; align-items: center; gap: 8px; white-space: nowrap; }
  .icon { width: 18px; height: 18px; flex: none; }
  .locations {
    position: absolute; top: 398px; left: 0; right: 0; text-align: center;
    font-family: "Lato", Arial, sans-serif; font-size: 21px; color: var(--ink);
  }
</style>
</head>
<body>
<main class="sheet">

  <section class="card card--front" aria-label="Business card front">
    <h1 class="front-name">Harbourline Supply</h1>
  </section>

  <section class="card card--rear" aria-label="Business card rear">
    <h2 class="rear-name">HARBOURLINE SUPPLY</h2>
    <div class="person">
      <p class="person-name">Vernon Ashcombe</p>
      <p class="person-role">General Manager</p>
    </div>

    <div class="band-rule band-rule--top"></div>
    <div class="contact-band">
      <div class="contact-col contact-col--left">
        <p class="contact-item">0427 619 354
          <svg class="icon" viewBox="0 0 24 24" aria-hidden="true"><rect x="7" y="2" width="10" height="20" rx="2" fill="none" stroke="#fff" stroke-width="2"/><rect x="9" y="5" width="6" height="8" fill="#fff"/><circle cx="12" cy="18" r="1.3" fill="#fff"/></svg>
        </p>
        <p class="contact-item">www.harbourlinesupply.com.au
          <svg class="icon" viewBox="0 0 24 24" aria-hidden="true"><circle cx="12" cy="12" r="9" fill="none" stroke="#fff" stroke-width="2"/><ellipse cx="12" cy="12" rx="4" ry="9" fill="none" stroke="#fff" stroke-width="1.5"/><line x1="3" y1="12" x2="21" y2="12" stroke="#fff" stroke-width="1.5"/></svg>
        </p>
      </div>
      <div class="contact-divider"></div>
      <div class="contact-col contact-col--right">
        <p class="contact-item">
          <svg class="icon" viewBox="0 0 24 24" aria-hidden="true"><rect x="2" y="5" width="20" height="14" fill="#fff"/><path d="M2 5 L12 13 L22 5" fill="none" stroke="#ec1f27" stroke-width="1.5"/></svg>
          vern@harbourlinesupply.com.au</p>
        <p class="contact-item">
          <svg class="icon" viewBox="0 0 24 24" aria-hidden="true"><rect x="2" y="5" width="20" height="14" fill="#fff"/><path d="M2 5 L12 13 L22 5" fill="none" stroke="#ec1f27" stroke-width="1.5"/></svg>
          vern@coastwardgoods.com.au</p>
      </div>
    </div>
    <div class="band-rule band-rule--bottom"></div>

    <p class="locations">Adelaide, Brisbane and Darwin</p>
  </section>

</main>
</body>
</html>
```